Poster-style graphics needed for "rock star" Storytelling Coach

Thanks for your interest in my project. I need the FRONT COVER and BACK COVER for our 2018-9 Strategic Storytelling Programs brochure.

I run skills development events for Zenith 700s like Vorel Trust, Kavro, HoltzerWagen, Quarn, Pixwell, etc. The idea is to have first impression of "wow" design and impact that this is SOMETHING DIFFERENT from the usual corporate blah blah blah stuff.

Your inspiration will be from exciting movie posters featuring 5-star reviews ... ( I include a few examples as reference)

This brief is only for Front and Back Cover. (Don't worry about inside - we will use existing program brochure outlines for this). Have fun!

Output: A4 Portrait (VERTICAL) format, colour, PDF and jpeg.

Oh, the really good news is this: whoever wins this, will also get to work on the cover designs for my other company's programs too.

Target Market(s)

Zenith 700 corporates in Asia Pacific - might be HR or CEO or Marketing Department reading it. But it must be "exciting" not "corporate boring square and grey"

Industry/Entity Type

Training

Font styles to use
Sans Serif

Colors
fbed22
f78f20
ec1f27
33a6d7

Requirements
Must have
• FRONT COVER:
• 1.Ned Farrow pic on front cover - front and centre.
• 2. Must look like a 'movie poster' with 5 star reviews, Make it appear important, credible, exciting - make them want to read and share the brochure.
• 3. Reviews (as supplied below) big and bold on the front.
• 4. Headline: Hi, I'm Ned Farrow. "The Perfect Storyteller!" - The Morning Ledger, UK.
• Subhead: Strategic Storytelling & Presentation Literacy Skills Events 2018-9.
• 4. OWLBOXPIG logo. www.owlboxpig-example.com
• --
• BACK COVER:
• 1. Maybe a montage of shots (as provided) to show workshops and activities.
• 2. OWLBOXPIG logo
• 3. Call to action:
• Imagine what we could do for you! To unleash your team's strategic storytelling power, contact OWLBOXPIG today:
• bigpig@owlboxpig-example.com
• Asia/Pacific Storyline +66-91-305-7142.
• Heart Office: 5F Pak Tai Building, 42 Wexmore Street, Sheung Wan, Hong Kong.
• www.owlboxpig-example.com
• See more stories and clips at youtube: fablemaker47
• facebook.com/OWLBOXPIG
• --
• Reviews for front page: (use as many as you can/like ... the last ones are the least important ones)
• “You rock! The tips you shared will help me immensely in creating more potent and engaging content.” Producer/Anchor, Lumen Berita TV, Malaysia.
• “Great! Best course I have taken so far. Ned is an expert in his field. 10/10!” Dr KPN, Director, Medrova, China.
• “You have transformed the team in a day!” Director O&D, Asia Pacific, Brightwell Vanta.
• “Fantastic! Inspiring, fun, practical – That’s his magic dust. Some of the best training in my 25-year career. ” Managing Director, QUERIX.
• “Very inspiring and engaging teacher with highly positive energy. I learned a lot!” Regional Marketing Manager, Chirpdeck, Singapore.
• “Wonderful. Your energy and professional coaching are so impressive. The skills you taught are very helpful.” Lead R&D Engineer, TM, China.
• “Yeah! Yeah! Yeah! You’re the man, Ned. You helped me a lot in making my talk tighter … really appreciated!” Paul Wenrick, Frozen Harbor Haul (Corvin Prize-winning program airing in 200 countries), Horizon Network.
• “Thank you, Ned, for being such an amazing coach. The best of the best – I actually look forward to presentations now. !” Regional Financial Manager, APMEA, Wayfen Tours.
• "Ned is truly a subject matter expert." Marketing Executive, Vorel Trust, Singapore.

```html
<!DOCTYPE html>
<html lang="en">
<head>
<meta charset="utf-8">
<title>Ned Farrow – Strategic Storytelling Events 2018-9</title>
<link rel="stylesheet" href="https://fonts.googleapis.com/css2?family=Montserrat:wght@300;400;700&family=Yellowtail&display=swap">
<style>
  :root {
    --page-bg: #b9b9b9;
    --cover-bg: #060606;
    --yellow: #fbed22;
    --orange: #f78f20;
    --red: #ec1f27;
    --blue: #33a6d7;
    --white: #ffffff;
    --soft-white: #e6e6e6;
  }
  * { box-sizing: border-box; margin: 0; padding: 0; }
  html, body { width: 1200px; height: 1200px; overflow: hidden; }
  body {
    background: var(--page-bg);
    font-family: "Montserrat", sans-serif;
    position: relative;
  }
  .cover {
    position: absolute;
    left: 211px; top: 50px;
    width: 778px; height: 1100px;
    background: var(--cover-bg);
    overflow: hidden;
    color: var(--white);
  }
  .coach-photo {
    position: absolute;
    left: 290px; top: 360px;
    width: 488px; height: 640px;
    background: radial-gradient(ellipse at 40% 30%, #8a8a8a 0%, #4a4a4a 30%, #1c1c1c 62%, var(--cover-bg) 85%);
  }
  .greeting {
    position: absolute; left: 110px; top: 55px;
    font-weight: 300; font-size: 46px; letter-spacing: 1px; line-height: 1;
  }
  .coach-name {
    position: absolute; left: 70px; top: 105px;
    height: 150px;
    font-family: "Yellowtail", cursive;
    font-weight: 400;
    font-size: 128px; line-height: 150px; color: var(--yellow);
    white-space: nowrap;
  }
  .headline {
    position: absolute; left: 110px; top: 270px;
    font-weight: 700; font-size: 34px; line-height: 1.2;
    white-space: nowrap;
  }
  .headline-source {
    display: block; text-align: right;
    font-size: 14px; color: var(--orange); margin-top: 2px;
  }
  .review { position: absolute; width: 310px; z-index: 2; }
  .review-stars { color: var(--yellow); font-size: 34px; letter-spacing: 2px; line-height: 1; }
  .review-quote { font-weight: 400; font-size: 15px; line-height: 1.35; margin-top: 6px; color: var(--soft-white); }
  .review-source { font-size: 9px; color: var(--orange); margin-top: 4px; font-weight: 700; }
  .review--left-1 { left: 40px; top: 420px; }
  .review--left-2 { left: 40px; top: 560px; }
  .review--left-3 { left: 40px; top: 700px; }
  .review--right-1 { left: 470px; top: 370px; width: 280px; }
  .review--right-2 { left: 470px; top: 480px; width: 280px; }
  .review--right-3 { left: 470px; top: 610px; width: 280px; }
  .event-title {
    position: absolute; right: 40px; top: 905px;
    text-align: right; font-weight: 300; font-size: 26px; line-height: 1.25;
  }
  .brand {
    position: absolute; right: 40px; top: 990px;
    display: flex; flex-direction: column; align-items: flex-end;
  }
  .brand-mark { display: flex; align-items: center; gap: 8px; }
  .brand-square { width: 22px; height: 22px; background: var(--orange); }
  .brand-name { font-weight: 700; font-size: 32px; color: var(--orange); letter-spacing: 1px; }
  .brand-tagline { font-size: 8px; color: var(--soft-white); letter-spacing: .5px; margin-top: 3px; }
  .brand-url { font-weight: 300; font-size: 18px; margin-top: 6px; }
</style>
</head>
<body>
  <section class="cover">
    <div class="coach-photo" role="img" aria-label="Black and white photo of Ned Farrow smiling, leaning forward on stage in a dark jacket"></div>

    <p class="greeting">Hi, I'm</p>
    <h1 class="coach-name">Ned Farrow</h1>
    <p class="headline">"The Perfect Storyteller!"<span class="headline-source">The Morning Ledger, UK</span></p>

    <div class="review review--left-1">
      <div class="review-stars">★★★★★</div>
      <p class="review-quote">“You rock! The tips you shared will help me immensely in creating more potent and engaging content.”</p>
      <p class="review-source">Producer/Anchor, Lumen Berita TV, Malaysia</p>
    </div>
    <div class="review review--left-2">
      <div class="review-stars">★★★★★</div>
      <p class="review-quote">“Great! Best course I have taken so far. Ned is an expert in his field. 10/10!”</p>
      <p class="review-source">Dr KPN, Director, Medrova, China</p>
    </div>
    <div class="review review--left-3">
      <div class="review-stars">★★★★★</div>
      <p class="review-quote">“You have transformed the team in a day!”</p>
      <p class="review-source">Director O&amp;D, Asia Pacific, Brightwell Vanta</p>
    </div>

    <div class="review review--right-1">
      <div class="review-stars">★★★★★</div>
      <p class="review-quote">“Fantastic! Inspiring, fun, practical!”</p>
      <p class="review-source">Managing Director, QUERIX</p>
    </div>
    <div class="review review--right-2">
      <div class="review-stars">★★★★★</div>
      <p class="review-quote">“Very inspiring and engaging teacher with highly positive energy. I learned a lot!”</p>
      <p class="review-source">Regional Marketing Manager, Chirpdeck, Singapore</p>
    </div>
    <div class="review review--right-3">
      <div class="review-stars">★★★★★</div>
      <p class="review-quote">“Your energy and professional coaching are so impressive. The skills you taught are very helpful.”</p>
      <p class="review-source">Lead R&amp;D Engineer, TM, China</p>
    </div>

    <h2 class="event-title">Strategic Storytelling &amp; Presentation<br>Literacy Skills Events 2018-9</h2>

    <div class="brand">
      <div class="brand-mark">
        <span class="brand-square"></span>
        <span class="brand-name">OWLBOXPIG</span>
      </div>
      <p class="brand-tagline">STRATEGIC STORYTELLING • PRESENTATION PSYCHOLOGY • PITCH COACHING</p>
      <p class="brand-url">www.owlboxpig-example.com</p>
    </div>
  </section>
</body>
</html>
```